Front cover for our tenth anniversary show programme

To create an eye catching tenth anniversary front cover for our programme

Moonbrook presents DANCE! 2015

date of the show Sunday 3rd May 2015

Venue The Harrowgate Stagehouse

please see the updated brief!

Reason: there hasn't been anything that is quite right

```html
<!DOCTYPE html>
<html lang="en">
<head>
<meta charset="utf-8">
<title>Moonbrook presents DANCE! 2015 – Programme Cover</title>
<link rel="stylesheet" href="https://fonts.googleapis.com/css2?family=Open+Sans:ital,wght@0,300;0,400;0,600;1,300;1,800&display=swap">
<style>
  :root {
    --bg-deep: #150306;
    --bg-mid: #3a0a16;
    --burst-core: #fff1f4;
    --burst-pink: #e0687f;
    --burst-rose: #8c1f3a;
    --accent-pink: #e4528f;
    --text-white: #ffffff;
    --silhouette: #0d0205;
  }
  html, body {
    margin: 0;
    padding: 0;
    width: 849px;
    height: 1200px;
    overflow: hidden;
    background: var(--bg-deep);
  }
  .cover {
    position: relative;
    width: 849px;
    height: 1200px;
    overflow: hidden;
    font-family: "Open Sans", Arial, sans-serif;
    color: var(--text-white);
    background:
      radial-gradient(circle at 50% 58%, var(--burst-core) 0%, var(--burst-pink) 8%, var(--burst-rose) 22%, var(--bg-mid) 42%, var(--bg-deep) 75%);
  }
  .light-rays {
    position: absolute;
    inset: 0;
    width: 849px;
    height: 1200px;
  }
  .brand {
    position: absolute;
    top: 78px;
    left: 0;
    width: 100%;
    text-align: center;
  }
  .brand-name {
    display: inline-flex;
    align-items: center;
    gap: 14px;
    font-weight: 600;
    font-size: 58px;
    line-height: 1;
    color: var(--text-white);
    letter-spacing: 0.5px;
  }
  .brand-mark {
    width: 30px;
    height: 30px;
    border-radius: 50%;
    background: var(--accent-pink);
  }
  .brand-tagline {
    margin-top: 12px;
    font-size: 20px;
    font-weight: 600;
    line-height: 1.2;
  }
  .brand-tagline .years {
    display: block;
    font-size: 32px;
    color: var(--text-white);
  }
  .dancer {
    position: absolute;
    left: 340px;
    top: 490px;
    width: 160px;
    height: 420px;
    border-radius: 80px 80px 40px 40px;
    background: radial-gradient(ellipse at 50% 45%, var(--silhouette) 55%, rgba(13,2,5,0) 100%);
  }
  .presenter {
    position: absolute;
    top: 828px;
    left: 0;
    width: 100%;
    text-align: center;
    font-style: italic;
    font-weight: 300;
    font-size: 28px;
  }
  .show-title {
    position: absolute;
    top: 940px;
    left: 0;
    width: 100%;
    text-align: center;
    margin: 0;
    font-style: italic;
    font-weight: 800;
    font-size: 84px;
    line-height: 1;
    letter-spacing: -1px;
  }
  .show-title .year {
    color: var(--accent-pink);
  }
  .show-date {
    position: absolute;
    top: 1098px;
    left: 0;
    width: 100%;
    text-align: center;
    font-weight: 300;
    font-size: 30px;
    letter-spacing: 1px;
  }
  .show-venue {
    position: absolute;
    top: 1142px;
    left: 0;
    width: 100%;
    text-align: center;
    font-weight: 300;
    font-size: 17px;
  }
</style>
</head>
<body>
<main class="cover">
  <svg class="light-rays" viewBox="0 0 849 1200" aria-hidden="true">
    <defs>
      <radialGradient id="ray-fade" cx="425" cy="700" r="520" gradientUnits="userSpaceOnUse">
        <stop offset="0" stop-color="#ffffff" stop-opacity="0.55"/>
        <stop offset="0.5" stop-color="#f08aa0" stop-opacity="0.18"/>
        <stop offset="1" stop-color="#f08aa0" stop-opacity="0"/>
      </radialGradient>
    </defs>
    <g fill="url(#ray-fade)">
      <polygon points="425,700 -40,430 -40,470"/>
      <polygon points="425,700 -40,640 -40,680"/>
      <polygon points="425,700 -40,860 -40,900"/>
      <polygon points="425,700 890,430 890,470"/>
      <polygon points="425,700 890,640 890,680"/>
      <polygon points="425,700 890,860 890,900"/>
      <polygon points="425,700 150,160 185,160"/>
      <polygon points="425,700 330,160 355,160"/>
      <polygon points="425,700 500,160 525,160"/>
      <polygon points="425,700 670,160 700,160"/>
      <polygon points="425,700 90,300 115,285"/>
      <polygon points="425,700 760,285 785,300"/>
      <polygon points="425,700 160,1150 190,1160"/>
      <polygon points="425,700 660,1160 690,1150"/>
    </g>
  </svg>

  <header class="brand">
    <div class="brand-name"><span class="brand-mark"></span>Moonbrook</div>
    <div class="brand-tagline">Celebrating<span class="years">Ten Years</span></div>
  </header>

  <div class="dancer" role="img" aria-label="Silhouette of a ballerina in a tutu, arms raised, standing on one leg"></div>

  <p class="presenter">Moonbrook presents</p>
  <h1 class="show-title">DANCE! <span class="year">2015</span></h1>
  <p class="show-date">SUNDAY 3RD MAY</p>
  <p class="show-venue">at The Harrowgate Stagehouse</p>
</main>
</body>
</html>
```